Professional Services/Construction Management (Millwork) Biz Cards

We've decided on a logo and have our color palette set, now we want to design some very professional looking cards that make a strong first impression - they'll reflect our tagline (that we're going to put on the back: Innovative. Professional. Leaders.

The example business card shows generally the direction we've been thinking of going for the back side - **but we're open to other ideas**

Target Market(s)

The cards should target more high-end (wealthy) owners and general contracting companies. We want them to convey a strong first impression - in a professional and not garish way.

Industry/Entity Type

Construction Company

Contact Information for Business Card

There needs to be a place for our company contractor's license number and business address. We want to also have people's names, titles, phone number, email address. The back can be the logo, tagline and web address

Requirements
Must have
• follow our color palette
Nice to have
• Font & Styles should compliment the Harrow Joinery fonts, but not necessarily match exactly

```html
<!DOCTYPE html>
<html lang="en">
<head>
<meta charset="utf-8">
<title>Harrow Joinery Business Cards</title>
<link rel="stylesheet" href="https://fonts.googleapis.com/css2?family=Exo+2:wght@400;600&display=swap">
<style>
  :root {
    --backdrop: #3a3431;
    --card-white: #ffffff;
    --card-black: #1b1b1b;
    --ink: #1e1e1e;
    --ink-light: #f2f2f2;
    --ink-muted: #cfcfcf;
  }
  * { margin: 0; padding: 0; box-sizing: border-box; }
  html, body { width: 1200px; height: 799px; overflow: hidden; }
  body {
    background: var(--backdrop);
    font-family: "Exo 2", sans-serif;
    position: relative;
  }
  .card {
    position: absolute;
    width: 520px;
    height: 300px;
    background: var(--card-white);
    overflow: hidden;
    box-shadow: 0 10px 24px rgba(0,0,0,.45);
  }
  .card-front { left: 50px; top: 140px; }
  .card-back { left: 630px; top: 360px; }
  .front-panel { position: absolute; inset: 0; }
  .brand {
    position: absolute;
    display: flex;
    align-items: center;
    gap: 10px;
    color: var(--ink);
    font-weight: 600;
    white-space: nowrap;
  }
  .brand-mark {
    border-radius: 50%;
    background: var(--card-black);
    flex: none;
  }
  .card-front .brand { left: 22px; top: 130px; font-size: 17px; }
  .card-front .brand-mark { width: 22px; height: 22px; }
  .card-back .brand { left: 170px; top: 118px; font-size: 26px; }
  .card-back .brand-mark { width: 34px; height: 34px; }
  .person {
    position: absolute;
    right: 28px;
    top: 40px;
    text-align: right;
    color: var(--ink-light);
  }
  .person-name { font-size: 22px; font-weight: 600; letter-spacing: .5px; }
  .person-title { font-size: 13px; color: var(--ink-muted); margin-top: 2px; }
  .contact {
    position: absolute;
    right: 28px;
    bottom: 30px;
    list-style: none;
    color: var(--ink-light);
    font-size: 12px;
    text-align: right;
  }
  .contact li {
    display: flex;
    justify-content: flex-end;
    align-items: center;
    gap: 8px;
    line-height: 21px;
  }
  .contact-icon { width: 11px; height: 11px; flex: none; }
  .tagline {
    position: absolute;
    left: 28px;
    bottom: 34px;
    font-size: 19px;
    color: var(--ink);
  }
</style>
</head>
<body>
  <section class="card card-front">
    <svg class="front-panel" viewBox="0 0 520 300" aria-hidden="true">
      <path d="M225,0 H520 V300 H150 Q285,160 225,0 Z" fill="var(--card-black)"/>
    </svg>
    <div class="brand"><span class="brand-mark"></span>Harrow Joinery</div>
    <div class="person">
      <p class="person-name">Daniel Reyes</p>
      <p class="person-title">Manager</p>
    </div>
    <ul class="contact">
      <li>Lic 20481937 <span class="contact-icon"></span></li>
      <li>45 6120 3384
        <svg class="contact-icon" viewBox="0 0 12 12"><rect width="12" height="12" rx="1" fill="#fff"/><path d="M3,3 h2 l1,2 -1,1 q1,2 2,2 l1,-1 2,1 v2 q-6,0 -7,-7z" fill="#1b1b1b"/></svg>
      </li>
      <li>hello@harrowjoinery.com
        <svg class="contact-icon" viewBox="0 0 12 12"><rect width="12" height="12" rx="1" fill="#fff"/><rect x="2" y="3.5" width="8" height="5" fill="none" stroke="#1b1b1b"/><path d="M2,3.5 6,6.5 10,3.5" fill="none" stroke="#1b1b1b"/></svg>
      </li>
      <li>58 Birchfield Lane, Ashford, VT 5821
        <svg class="contact-icon" viewBox="0 0 12 12"><rect width="12" height="12" rx="1" fill="#fff"/><path d="M6,10 Q3,6.5 3,5 a3,3 0 0 1 6,0 Q9,6.5 6,10z" fill="#1b1b1b"/><circle cx="6" cy="5" r="1" fill="#fff"/></svg>
      </li>
    </ul>
  </section>

  <section class="card card-back">
    <div class="brand"><span class="brand-mark"></span>Harrow Joinery</div>
    <p class="tagline">Construction Management (Millwork) Biz</p>
  </section>
</body>
</html>
```